Webdesign/Updates

We would like a landing page for an online course for our educators. So a website with about 3 to 5 pages - Home, About US, Online course, blog, and Contact us. We have a wordpress site up using a template, but we are looking for something that connects more with our new logo.

Target Market(s)

Educators, workshop trainers/instructors, colleges, community schools, educational institutions, global organizations

Industry/Entity Type

Education

Contact Information for Business Card

Use the words below as place holders for the front:
Name
Title
Address line 1
Address line 2
Email
Phone
Website URL

--the back
Logo
1 short question, use "What do you 1234 about your program?"

Number of Pages Required

4 page

Requirements
Must have
• Home page
• Course Page
• Blog
• right side bar with social media content and invitation to subscribe to newsletter
• see logo colors in document
Nice to have
• Newsletter Page with graphic that can be on this page or page can be sent as a pdf via email or in an email.
Should not have
• Be better than attached description
• clean simple look but stylish

```html
<!DOCTYPE html>
<html lang="en">
<head>
<meta charset="utf-8">
<title>Brightpath Learning — Online Courses for Educators</title>
<link rel="stylesheet" href="https://fonts.googleapis.com/css2?family=Lato:wght@300;400;700;900&family=Tinos:wght@400;700&display=swap">
<style>
:root{
  --accent:#ec5a2a;
  --accent-dark:#d94a1c;
  --ink:#333333;
  --text:#555555;
  --muted:#9a9a9a;
  --line:#e6e6e6;
  --soft:#f4f4f4;
  --footer:#2d3142;
  --green:#8cc63f;
  --star:#e8432b;
  --share-1:#3b5998;
  --share-2:#1da1f2;
  --share-3:#dd4b39;
  --share-4:#cb2027;
  --white:#ffffff;
}
*{box-sizing:border-box;margin:0;padding:0}
html,body{width:1200px;height:4592px;overflow:hidden}
body{position:relative;background:var(--white);font-family:"Lato",Arial,sans-serif;color:var(--text)}
.abs{position:absolute}

/* hero */
.hero{position:absolute;left:0;top:0;width:1200px;height:872px;
  clip-path:polygon(0 0,100% 0,100% 658px,50% 872px,0 658px);
  background:linear-gradient(110deg,#6d5e56 0%,#8b7a6c 30%,#5d6f86 60%,#3d4f68 100%)}
.hero::after{content:"";position:absolute;inset:0;background:rgba(20,30,50,.35)}
.brand{position:absolute;left:64px;top:76px;display:flex;align-items:center;gap:14px;z-index:2;
  color:var(--white);font-weight:700;font-size:36px}
.brand-dot{width:30px;height:30px;border-radius:50%;background:var(--green)}
.nav{position:absolute;right:64px;top:82px;display:flex;gap:22px;z-index:2}
.nav a{color:var(--white);text-decoration:none;font-weight:700;font-size:21px}
.hero-title{position:absolute;left:62px;top:262px;z-index:2;color:var(--white);font-weight:700;font-size:88px;letter-spacing:-1px}
.hero-lead{position:absolute;left:64px;top:368px;width:700px;z-index:2;color:var(--white);font-size:25px;line-height:33px}
.btn{display:inline-block;background:var(--accent);color:var(--white);font-weight:700;text-transform:uppercase;
  font-size:20px;text-align:center;border-radius:30px}
.hero .btn{position:absolute;left:64px;top:487px;width:238px;height:56px;line-height:56px;z-index:2}

/* share rail */
.share{position:absolute;left:0;top:1046px;width:86px;z-index:5}
.share-item{height:89px;display:flex;flex-direction:column;align-items:center;justify-content:center;gap:6px;color:var(--white);font-weight:700;font-size:24px}
.share-item .glyph{width:22px;height:22px;border-radius:4px;background:rgba(255,255,255,.85)}
.share-item:nth-child(1){background:var(--share-1)}
.share-item:nth-child(2){background:var(--share-2)}
.share-item:nth-child(3){background:var(--share-3)}
.share-item:nth-child(4){background:var(--share-4);border-radius:0 0 10px 0}

/* section headings */
.sec-title{position:absolute;left:0;width:1200px;text-align:center;font-family:"Tinos",Georgia,serif;font-size:60px;color:var(--ink)}
.sec-sub{position:absolute;left:0;width:1200px;text-align:center;font-size:29px;color:var(--muted)}

/* featured */
.video{position:absolute;left:214px;top:1040px;width:771px;height:466px;
  background:linear-gradient(135deg,#9fb4c2 0%,#c9d6dd 45%,#6f8797 100%);box-shadow:0 8px 18px rgba(0,0,0,.18)}
.play{position:absolute;left:50%;top:50%;width:100px;height:100px;margin:-50px 0 0 -50px;border-radius:50%;background:rgba(25,30,40,.85)}
.play svg{position:absolute;left:36px;top:28px}
.intro{position:absolute;left:140px;top:1547px;width:920px;text-align:center;font-size:26px;line-height:36px;color:var(--text)}
.featured-btn{position:absolute;left:481px;top:1725px;width:238px;height:58px;line-height:58px}
.slider-arrows{position:absolute;left:1068px;top:1791px;display:flex;gap:12px}
.slider-arrows span{width:30px;height:30px;border:2px solid #888;border-radius:50%;display:flex;align-items:center;justify-content:center}

.course{position:absolute;top:1845px;width:337px;height:490px;background:var(--white);box-shadow:0 2px 10px rgba(0,0,0,.08)}
.course-media{height:165px}
.course-badge{position:absolute;right:16px;top:224px;width:48px;height:48px;border-radius:50%;background:var(--green);color:var(--white);font-size:11px;font-weight:700;display:flex;align-items:center;justify-content:center;border:3px solid #fff}
.course-cat{position:absolute;top:246px;width:100%;text-align:center;color:var(--green);font-size:13px;font-weight:700}
.course-title{position:absolute;top:265px;width:100%;text-align:center;font-family:"Tinos",Georgia,serif;font-weight:700;font-size:20px;color:var(--ink)}
.course-rating{position:absolute;top:297px;width:100%;text-align:center;font-size:12px;color:var(--muted)}
.course-rating b{color:var(--star);font-size:17px;letter-spacing:1px;margin-right:6px}
.course-desc{position:absolute;top:352px;left:30px;right:30px;text-align:center;font-size:13px;line-height:17px;color:var(--muted)}
.course-stats{position:absolute;left:0;bottom:0;width:100%;height:66px;background:var(--soft);display:flex;padding:14px 12px 0}
.course-stats div{flex:1;font-size:11px;color:var(--muted);line-height:19px;border-right:1px solid var(--line);padding-left:6px}
.course-stats div:last-child{border-right:0}
.course-stats strong{display:block;color:var(--ink);font-weight:700}

/* program features */
.feature{position:absolute;width:230px}
.feature h3{font-family:"Tinos",Georgia,serif;font-weight:400;font-size:21px;color:#666;display:flex;align-items:center;gap:10px;margin-bottom:4px}
.feature h3 i{display:inline-block;width:18px;height:18px;border:2px solid #888;border-radius:3px}
.feature p{font-size:14px;line-height:19px;color:var(--muted)}
.feature.is-active{background:var(--white);box-shadow:0 4px 16px rgba(0,0,0,.16);padding:18px 20px}
.program-art{position:absolute;left:459px;top:2525px;width:245px;height:229px;border-radius:16px;
  background:linear-gradient(135deg,#3aa7e0 0%,#7fcff2 50%,#f2b63d 100%)}

/* testimonial */
.testimonial{position:absolute;left:214px;top:2929px;width:771px;height:459px;background:var(--white);box-shadow:0 4px 20px rgba(0,0,0,.14)}
.avatar{position:absolute;left:508px;top:2855px;width:184px;height:184px;border-radius:50%;border:6px solid #fff;
  background:linear-gradient(160deg,#5a4538 0%,#c9a48c 60%,#eee 100%);z-index:2;box-shadow:0 2px 8px rgba(0,0,0,.15)}
.person{position:absolute;left:214px;top:3040px;width:771px;text-align:center;font-weight:900;font-size:54px;color:#7a7a7a}
.person-role{position:absolute;left:214px;top:3104px;width:771px;text-align:center;font-size:29px;color:#7a7a7a}
.quote{position:absolute;left:264px;top:3158px;width:671px;text-align:center;font-size:25px;line-height:37px;color:var(--text)}
.dots{position:absolute;left:586px;top:3334px;display:flex;gap:8px}
.dots span{width:13px;height:13px;border-radius:50%;border:2px solid #9fc8ea}
.dots span.on{background:#1e88e5;border-color:#1e88e5}

/* blog */
.post{position:absolute;top:3565px;width:337px;height:551px;background:var(--white)}
.post-media{height:220px}
.post-meta{position:absolute;top:244px;left:0;font-size:15px;color:#777;white-space:nowrap}
.post-title{position:absolute;top:280px;left:0;font-family:"Tinos",Georgia,serif;font-weight:700;font-size:24px;line-height:34px;color:var(--ink)}
.post-body{position:absolute;top:383px;left:0;width:320px;font-size:16px;line-height:22px;color:#666}
.post-btn{position:absolute;top:502px;left:0;width:200px;height:50px;line-height:50px;font-size:18px}
.post-btn.is-muted{background:#b5b5b5}

/* footer */
.footer{position:absolute;left:0;top:4180px;width:1200px;height:412px;background:var(--footer)}
.footer h2{position:absolute;top:62px;width:100%;text-align:center;color:var(--white);font-weight:900;font-size:30px}
.signup{position:absolute;left:321px;top:126px;width:560px;height:54px;display:flex}
.signup span{flex:1;background:var(--white);border-radius:27px 0 0 27px;font-size:17px;color:#999;padding:16px 24px}
.signup b{width:184px;background:var(--accent);color:var(--white);border-radius:0 27px 27px 0;font-size:18px;font-weight:400;text-align:center;line-height:54px}
.footer-social{position:absolute;left:489px;top:280px;display:flex;gap:19px}
.footer-social span{width:42px;height:42px;border-radius:50%;background:var(--accent)}
.copyright{position:absolute;top:348px;width:100%;text-align:center;color:var(--white);font-size:17px}
</style>
</head>
<body>

<header class="hero" role="img" aria-label="Photo of a young woman working on a laptop at a desk, talking on the phone">
  <div class="brand"><span class="brand-dot"></span>Brightpath Learning</div>
  <nav class="nav"><a href="#">About US</a><a href="#">Online Course</a><a href="#">Blog</a><a href="#">Contact us</a></nav>
  <h1 class="hero-title">Brightpath Learning</h1>
  <p class="hero-lead">Lorem ipsum dolor sit amet, consectetur adipisicing do eiusmod tempor incididunt ut labore et do e magna aliqua. Ut enim a</p>
  <span class="btn">Get Started</span>
</header>

<aside class="share" aria-label="Share counts">
  <div class="share-item"><span class="glyph"></span>101</div>
  <div class="share-item"><span class="glyph"></span></div>
  <div class="share-item"><span class="glyph"></span>78</div>
  <div class="share-item"><span class="glyph"></span>86</div>
</aside>

<h2 class="sec-title" style="top:896px">Our Featured Courses</h2>
<p class="sec-sub" style="top:964px">Lorem ipsum dolor sit amet  consectetur adipiscing elit</p>

<div class="video" role="img" aria-label="Video still of a person using a laptop showing a course dashboard">
  <div class="play"><svg width="36" height="44" viewBox="0 0 36 44"><path d="M0 0 L36 22 L0 44 Z" fill="#fff"/></svg></div>
</div>

<p class="intro">orem ipsum dolor sit amet, consectetur adipiscing elit. Duis eu justo sed lacus convallis pulvinar et vitae tellus. Curabitur iaculis imperdiet massa, et feugiat urna vulputate nec. Donec tincidunt lacinia metus elementum volutpat. Nulla vestib</p>
<span class="btn featured-btn">Get Started</span>
<div class="slider-arrows">
  <span><svg width="10" height="14" viewBox="0 0 10 14"><path d="M8 1 L2 7 L8 13" stroke="#777" stroke-width="2" fill="none"/></svg></span>
  <span><svg width="10" height="14" viewBox="0 0 10 14"><path d="M2 1 L8 7 L2 13" stroke="#777" stroke-width="2" fill="none"/></svg></span>
</div>

<article class="course" style="left:64px">
  <div class="course-media" role="img" aria-label="Photo of electrical substation equipment" style="background:linear-gradient(180deg,#9aa6b3,#5c4a3d)"></div>
  <span class="course-badge">NEW</span>
  <div class="course-cat">Science</div>
  <h3 class="course-title">Electrical Engineering</h3>
  <div class="course-rating"><b>★★★★★</b>25 Reviews</div>
  <p class="course-desc">Cras ultricies lacus consectetur, consectetur scelerisque arcu curabitur</p>
  <div class="course-stats"><div><strong>Course Time</strong>2 Years</div><div><strong>Course Student</strong>30</div><div><strong>Class Duration</strong>$ 20.40</div></div>
</article>
<article class="course" style="left:431px">
  <div class="course-media" role="img" aria-label="Photo of a desk with a computer monitor and office items" style="background:linear-gradient(180deg,#d8d2c8,#8b5a3c)"></div>
  <span class="course-badge">NEW</span>
  <div class="course-cat">Science</div>
  <h3 class="course-title">Computer Engineering</h3>
  <div class="course-rating"><b>★★★★★</b>36 Reviews</div>
  <p class="course-desc">Cras ultricies lacus consectetur, consectetur scelerisque arcu curabitur</p>
  <div class="course-stats"><div><strong>Course Time</strong>3 Years</div><div><strong>Course Student</strong>30</div><div><strong>Class Duration</strong>$ 20.40</div></div>
</article>
<article class="course" style="left:799px">
  <div class="course-media" role="img" aria-label="Photo of a concrete dam with intake towers" style="background:linear-gradient(180deg,#b9c6d2,#6e5a4a)"></div>
  <span class="course-badge">NEW</span>
  <div class="course-cat">Science</div>
  <h3 class="course-title">Civil Engineering</h3>
  <div class="course-rating"><b>★★★★★</b>22 Reviews</div>
  <p class="course-desc">Cras ultricies lacus consectetur, consectetur scelerisque arcu curabitur</p>
  <div class="course-stats"><div><strong>Course Time</strong>2.5 Years</div><div><strong>Course Student</strong>30</div><div><strong>Class Duration</strong>$ 20.40</div></div>
</article>

<h2 class="sec-title" style="top:2374px">Program Feature</h2>
<p class="sec-sub" style="top:2446px">Lorem ipsum dolor sit amet  consectetur adipiscing elit</p>

<svg class="abs" style="left:290px;top:2540px" width="620" height="240" viewBox="0 0 620 240">
  <path d="M0 30 C90 10 140 20 170 70" stroke="#333" stroke-width="4" stroke-dasharray="1 11" stroke-linecap="round" fill="none"/>
  <path d="M0 225 C90 225 140 215 170 170" stroke="#333" stroke-width="4" stroke-dasharray="1 11" stroke-linecap="round" fill="none"/>
  <path d="M420 70 C460 20 520 20 580 30" stroke="#333" stroke-width="4" stroke-dasharray="1 11" stroke-linecap="round" fill="none"/>
  <path d="M420 170 C460 215 520 225 600 225" stroke="#333" stroke-width="4" stroke-dasharray="1 11" stroke-linecap="round" fill="none"/>
</svg>
<div class="program-art" role="img" aria-label="Illustration of a laptop surrounded by learning icons"></div>

<div class="feature" style="left:61px;top:2510px"><h3><i></i>Effective Lessons</h3><p>Lorem ipsum dolor sit amet, consectetur adipiscing elit. Duis eu justo sed lacus convallis pulvinar et vitae tellus. Curabitur iaculis imperdiet volutpat</p></div>
<div class="feature" style="left:61px;top:2694px"><h3><i></i>Quality Videos</h3><p>Lorem ipsum dolor sit amet, consectetur adipiscing elit. Duis eu justo sed lacus convallis pulvinar et vitae tellus. Curabitur iaculis imperdiet volutpat</p></div>
<div class="feature is-active" style="left:846px;top:2500px;width:292px"><h3><i></i>Awesome Quizzes</h3><p>Lorem ipsum dolor sit amet, consectetur adipiscing elit. Duis eu justo sed lacus convallis pulvinar et vitae tellus. Curabitur iaculis imperdiet volutpat</p></div>
<div class="feature" style="left:884px;top:2694px"><h3><i></i>Hosted Content</h3><p>Lorem ipsum dolor sit amet, consectetur adipiscing elit. Duis eu justo sed lacus convallis pulvinar et vitae tellus. Curabitur iaculis imperdiet volutpat</p></div>

<section class="testimonial" aria-label="Testimonial"></section>
<div class="avatar" role="img" aria-label="Portrait photo of the reviewer"></div>
<div class="person">Daniel Reyes</div>
<div class="person-role">Lorem ipsum</div>
<p class="quote">Lorem ipsum dolor sit amet, consectetur adipiscing elit. Duis eu justo sed lacus convallis pulvinar et vitae tellus. Curabitur iaculis imperdiet massa, et feugiat urna vulputate nec. Donec tincidunt lacinia metus eleme</p>
<div class="dots"><span class="on"></span><span></span></div>

<h2 class="sec-title" style="top:3421px">Blog</h2>
<p class="sec-sub" style="top:3490px">Lorem ipsum dolor sit amet  consectetur adipiscing elit</p>

<article class="post" style="left:64px">
  <div class="post-media" role="img" aria-label="Photo of a hand wearing a smartwatch" style="background:linear-gradient(135deg,#d9e6e6,#7fa3a6)"></div>
  <div class="post-meta">By Admin &nbsp;&nbsp;Janu, 15 2017 &nbsp;&nbsp;(20) Comments</div>
  <h3 class="post-title">How To Showcase Your<br>Awesome App?</h3>
  <p class="post-body">Lorem ipsum dolor sit amet, consectetur adipiscing elit, sed do eiusmod tempor incididunt ut labore et dolore magna aliqua. Ut enim ad minim veniam, quis nostrud exercitation.</p>
  <span class="btn post-btn">Get Started</span>
</article>
<article class="post" style="left:431px">
  <div class="post-media" role="img" aria-label="Photo of a phone with earphones on a desk" style="background:linear-gradient(135deg,#5b6470,#1f252d)"></div>
  <div class="post-meta">By Admin &nbsp;&nbsp;Janu, 15 2017 &nbsp;&nbsp;(20) Comments</div>
  <h3 class="post-title">How To Showcase Your<br>Awesome App?</h3>
  <p class="post-body">Lorem ipsum dolor sit amet, consectetur adipiscing elit, sed do eiusmod tempor incididunt ut labore et dolore magna aliqua. Ut enim ad minim veniam, quis nostrud exercitation.</p>
  <span class="btn post-btn is-muted">Get Started</span>
</article>
<article class="post" style="left:799px">
  <div class="post-media" role="img" aria-label="Photo of friends raising their arms near a bridge" style="background:linear-gradient(180deg,#d7dde6,#8c6f62)"></div>
  <div class="post-meta">By Admin &nbsp;&nbsp;Janu, 15 2017 &nbsp;&nbsp;(20) Comments</div>
  <h3 class="post-title">How To Showcase Your<br>Awesome App?</h3>
  <p class="post-body">Lorem ipsum dolor sit amet, consectetur adipiscing elit, sed do eiusmod tempor incididunt ut labore et dolore magna aliqua. Ut enim ad minim veniam, quis nostrud exercitation.</p>
  <span class="btn post-btn is-muted">Get Started</span>
</article>

<footer class="footer">
  <h2>SUBSCRIBE OUR NEWSLETTER</h2>
  <div class="signup"><span>Your email address here...</span><b>Subscribe</b></div>
  <div class="footer-social"><span></span><span></span><span></span><span></span></div>
  <p class="copyright">@ 2018 Copy Right. All Right Reserved.</p>
</footer>

</body>
</html>
```